Pawsome Tonic - Functtional water for dogs. Brand new product

I have a design alreday. It needs an upgrade. I need it in two steps. One that sums everything in 5 pges and one as the one as sent as the longer brief. So one that is a full version and one summary. I want it to be rea professional for a presentation to investors, stores etc. Important to make the same thur out the presentation so it feels like it belongs together. High end business but still modern for a brand new unique product. The first product on the market is Morning Minerals (the other 3 mighgt come later on). Its in Sweden we start like a city like stockholm. Important that its realistic. Not to dark. Again think towards high end investors.

Target Market(s)

The presentation is for investors och businesses. The product is for dogowners who keep their animals as family members, active people, city people, people who travel etc

Industry/Entity Type

Dogs och dog food and vitamins

Requirements
Must have
• High end but still modern and breathe a brand new product thats unique. For investors that will invest money in this project.

```html
<!DOCTYPE html>
<html lang="en">
<head>
<meta charset="utf-8">
<title>Pawsome Tonic – Investor Deck</title>
<link href="https://fonts.googleapis.com/css2?family=Signika:wght@400;600;700&family=Open+Sans:wght@400;600;700&display=swap" rel="stylesheet">
<style>
  :root{
    --brand-blue:#1b3fa8;
    --sky-blue:#6b96cd;
    --sky-deep:#4f7fc0;
    --ink:#111216;
    --white:#ffffff;
    --mist:#d8d8d8;
    --mist-light:#ececec;
    --skill-bg:#e8edf6;
  }
  *{margin:0;padding:0;box-sizing:border-box}
  html,body{width:1200px;height:747px;overflow:hidden;background:var(--white)}
  body{position:relative;font-family:"Open Sans",sans-serif;color:var(--ink)}
  .slide{position:absolute;width:514px;height:289px;overflow:hidden;box-shadow:0 6px 14px rgba(0,0,0,.18)}
  .slide--cover-light{left:75px;top:72px;background:linear-gradient(180deg,var(--mist-light),#cfcfcf)}
  .slide--cover-blue{left:616px;top:72px;background:var(--sky-blue)}
  .slide--contents{left:75px;top:389px;background:var(--white)}
  .slide--founder{left:616px;top:389px;background:var(--white)}
  .abs{position:absolute}
  .wordmark{position:absolute;font-family:"Signika",sans-serif;font-weight:700;line-height:1;display:flex;align-items:center;gap:4px;white-space:nowrap}
  .wordmark .dot{width:7px;height:7px;border-radius:50%;background:currentColor}
  .photo{position:absolute}
  .eyebrow{position:absolute;font-family:"Open Sans",sans-serif;font-size:12.5px;letter-spacing:.3px}
  .title{position:absolute;font-family:"Signika",sans-serif;font-weight:700;font-size:23px;line-height:26px}
  .accent-bar{position:absolute;width:34px;height:3px;border-radius:2px}
  .url{position:absolute;font-size:8px}
  .top-band{position:absolute;left:0;top:0;width:100%;height:5px;background:var(--brand-blue)}
  .top-band::before{content:"";position:absolute;left:0;top:0;width:134px;height:5px;background:var(--ink)}
  .footer-note{position:absolute;left:16px;top:277px;font-size:6.5px}
  .footer-note b{color:var(--brand-blue)}
  .page-pill{position:absolute;left:458px;top:268px;width:56px;height:16px;border-radius:8px 0 0 8px;background:var(--brand-blue);color:var(--white);font-size:7px;display:flex;align-items:center;justify-content:center}
  .toc-title{position:absolute;left:286px;top:86px;font-family:"Signika",sans-serif;font-weight:700;font-size:22px;line-height:20px}
  .toc-title span{color:var(--brand-blue);display:block}
  .toc-list{position:absolute;list-style:none;font-size:10px;line-height:16.2px}
  .toc-list b{color:var(--brand-blue);font-weight:400;margin-right:4px}
  .founder-name{position:absolute;left:0;width:170px;top:149px;text-align:center;font-family:"Signika",sans-serif;font-weight:700;font-size:17px}
  .role-pill{position:absolute;left:44px;top:175px;width:80px;height:19px;border-radius:10px;background:var(--brand-blue);color:var(--white);font-family:"Signika",sans-serif;font-weight:600;font-size:8px;display:flex;align-items:center;justify-content:center}
  .bio{position:absolute;left:166px;top:59px;width:310px;font-size:7.6px;line-height:9.7px}
  .bio p{margin-bottom:9.5px}
  .skills{position:absolute;left:169px;top:203px;width:171px}
  .skills__head{height:21px;background:var(--ink);color:var(--white);border-radius:6px 6px 0 0;font-family:"Signika",sans-serif;font-weight:600;font-size:8px;padding:6px 0 0 18px}
  .skills__row{display:flex;background:var(--skill-bg);height:32px;border-radius:0 0 6px 6px;font-size:7.6px;line-height:9.5px;color:var(--brand-blue)}
  .skills__row div{display:flex;gap:3px;padding:6px 4px 0 5px;border-right:1px solid var(--white)}
  .skills__row div:last-child{border-right:none}
  .skills__icon{position:absolute;left:-5px;top:-6px;width:20px;height:20px;border-radius:50%;background:var(--white);border:1.5px solid var(--brand-blue)}
</style>
</head>
<body>

<!-- Cover, light -->
<section class="slide slide--cover-light">
  <div class="photo" role="img" aria-label="Jumping beagle with a bottle of Morning Minerals dog water" style="left:0;top:0;width:300px;height:289px;background:radial-gradient(circle at 200px 230px,var(--sky-deep) 0,#8fb0d8 70px,rgba(200,200,200,0) 110px),linear-gradient(180deg,#e6e2dc,#c9b9a8 60%,#b9c7da)"></div>
  <div class="wordmark" style="left:404px;top:32px;font-size:14px;color:var(--ink)"><span class="dot"></span>Pawsome Tonic</div>
  <div class="eyebrow" style="left:315px;top:103px;color:var(--white)">PAWSOME TONIC</div>
  <div class="title" style="left:315px;top:124px"><span style="color:var(--ink)">The Future of</span><br><span style="color:var(--brand-blue)">Functional Pet<br>Hydration</span></div>
  <div class="accent-bar" style="left:317px;top:210px;background:var(--white)"></div>
  <div class="url" style="left:315px;top:272px;color:var(--white)">pawsometonic.com</div>
</section>

<!-- Cover, blue -->
<section class="slide slide--cover-blue">
  <div class="photo" role="img" aria-label="Jumping beagle on a blue studio backdrop" style="left:20px;top:30px;width:220px;height:259px;background:radial-gradient(ellipse at 50% 45%,#c89a6e 0,#a98a75 40px,rgba(107,150,205,0) 110px)"></div>
  <div class="photo" role="img" aria-label="Bottle of Morning Minerals dog water" style="left:438px;top:131px;width:58px;height:158px;border-radius:12px 12px 0 0;background:linear-gradient(180deg,#e8eef6 0,#e8eef6 30%,var(--brand-blue) 32%,#1d3c9a)"></div>
  <div class="wordmark" style="left:404px;top:32px;font-size:14px;color:var(--white)"><span class="dot"></span>Pawsome Tonic</div>
  <div class="eyebrow" style="left:259px;top:87px;color:var(--brand-blue)">PAWSOME TONIC</div>
  <div class="title" style="left:259px;top:108px"><span style="color:var(--ink)">The Future of</span><br><span style="color:var(--white)">Functional Pet<br>Hydration</span></div>
  <div class="accent-bar" style="left:261px;top:194px;background:var(--brand-blue)"></div>
  <div class="url" style="left:259px;top:272px;color:var(--brand-blue)">pawsometonic.com</div>
</section>

<!-- Table of contents -->
<section class="slide slide--contents">
  <div class="top-band"></div>
  <div class="wordmark" style="left:440px;top:20px;font-size:9px;color:var(--ink)"><span class="dot" style="width:5px;height:5px"></span>Pawsome Tonic</div>
  <div class="photo" role="img" aria-label="Smiling woman hugging a brown labrador in a park" style="left:0;top:53px;width:272px;height:179px;border-radius:0 90px 90px 0;background:linear-gradient(120deg,#5f7a45,#6b5442 55%,#4a3328)"></div>
  <h2 class="toc-title"><span>Table of</span>Contents</h2>
  <ol class="toc-list" style="left:288px;top:131px">
    <li><b>1.</b>Owner</li><li><b>2.</b>Why</li><li><b>3.</b>Target group</li><li><b>4.</b>Product</li>
  </ol>
  <ol class="toc-list" style="left:386px;top:131px">
    <li><b>5.</b>Sustainability</li><li><b>6.</b>Identity</li><li><b>7.</b>Market opportunity</li><li><b>8.</b>Offer and OT</li>
  </ol>
  <div class="footer-note"><b>PawsomeTonic</b>. All Rights Reserved © 2026</div>
  <div class="page-pill">2</div>
</section>

<!-- Founder -->
<section class="slide slide--founder">
  <div class="top-band"></div>
  <div class="wordmark" style="left:440px;top:20px;font-size:9px;color:var(--ink)"><span class="dot" style="width:5px;height:5px"></span>Pawsome Tonic</div>
  <div class="photo" role="img" aria-label="Black and white portrait of the founder outdoors" style="left:42px;top:60px;width:84px;height:84px;border-radius:50%;background:radial-gradient(circle at 55% 45%,#c9c9c9,#555 70%)"></div>
  <div class="founder-name">Erik Lindqvist</div>
  <div class="role-pill">CEO/ Founder</div>
  <div class="bio">
    <p>Erik Lindqvist founded Northfield Sweden AB in 2021. Erik have since 2023 been developing the concept for *Pawsome Tonic* as a product of Northfield Sweden.</p>
    <p>With over 20 years of experience in marketing, Erik has held leadership roles, including Head of Marketing for a prominent hunting organization in Sweden. During 2024 he lead a department in a billiondollar retail and outdoor company. Erik possesses deep expertise in branding, customer insights, PR, and strategic B2C marketing.</p>
    <p>Over the past decade, he has played a key role in influencing hunting policiesin Sweden and across Europe through strategic lobbying efforts. As an entrepreneur with a passion for business development, Erik brings a forward-thinking, results-driven approach to every endeavor.</p>
  </div>
  <div class="skills">
    <div class="skills__icon"></div>
    <div class="skills__head">Top skills</div>
    <div class="skills__row">
      <div style="width:74px"><span>⊘</span><span>Business Development</span></div>
      <div style="width:32px"><span>⊘</span><span>PR</span></div>
      <div style="flex:1"><span>⊘</span><span>Customer Experience</span></div>
    </div>
  </div>
  <div class="footer-note"><b>PawsomeTonic</b>. All Rights Reserved © 2026</div>
  <div class="page-pill">1</div>
</section>

</body>
</html>
```